4 Page Price List with Photos - 8.5"x17" Folded Once - 2017

Our price list should include our company logo, company information (provided), and our price list (excel file that must be formatted). Photos can be used as the designer likes. Design look is up to the designer. 4 pages, full color - output needed in PDF only - high res for printing and low res for email. Standard 8.5"x11" pages which will be 11x17 folded.

Correct price list file is now posted to project (8/9/66 8:32 Pacific Time)

Target Market(s)

Our regular customers

Font styles to use
Serif

Requirements
Must have
• Eye catching and professional design. Must show off our company logo. Please use black and gold as the main colors.
Nice to have
• Use only photos that look good in the design
Should not have
• Weird fonts or confusing format

```html
<!DOCTYPE html>
<html lang="en">
<head>
<meta charset="utf-8">
<title>Price List</title>
<link rel="stylesheet" href="https://fonts.googleapis.com/css2?family=Arimo:wght@700&display=swap">
<style>
  :root {
    --backdrop: #231f20;
    --sheet: #ffffff;
    --header-bg: #151515;
    --header-ink: #ffffff;
    --ink: #222222;
    --spec-bg: #efefef;
    --rule: #e6e6e6;
  }
  html, body {
    margin: 0;
    padding: 0;
    width: 1200px;
    height: 1000px;
    overflow: hidden;
    background: var(--backdrop);
  }
  .sheet {
    position: absolute;
    left: 48px;
    top: 33px;
    width: 1152px;
    height: 967px;
    overflow: hidden;
    background: var(--sheet);
    font-family: 'Arimo', Arial, Helvetica, sans-serif;
    font-weight: 700;
  }
  .col-head {
    position: absolute;
    top: 12px;
    height: 64px;
    background: var(--header-bg);
    color: var(--header-ink);
    font-size: 37px;
    letter-spacing: 1.5px;
    line-height: 66px;
    white-space: nowrap;
    overflow: hidden;
  }
  .col-head.description { left: 16px; width: 864px; text-align: center; }
  .col-head.price-spec { left: 892px; width: 260px; padding-left: 212px; box-sizing: border-box; }
  .spec-column {
    position: absolute;
    left: 887px;
    top: 82px;
    width: 265px;
    height: 885px;
    background: var(--spec-bg);
  }
  .price-table {
    position: absolute;
    left: 0;
    top: 94px;
    width: 1152px;
    list-style: none;
    margin: 0;
    padding: 0;
  }
  .price-row {
    display: flex;
    height: 49.8px;
    border-bottom: 2px solid var(--rule);
    box-sizing: border-box;
    color: var(--ink);
    font-size: 35px;
    letter-spacing: 1px;
    line-height: 50px;
    white-space: nowrap;
    overflow: hidden;
  }
  .product {
    flex: 0 0 887px;
    width: 887px;
    padding-left: 15px;
    box-sizing: border-box;
    overflow: hidden;
  }
  .spec {
    flex: 0 0 auto;
    padding-left: 48px;
  }
</style>
</head>
<body>
  <div class="sheet">
    <div class="spec-column"></div>
    <div class="col-head description">PRODUCT DESCRIPTION</div>
    <div class="col-head price-spec">PRODUCT SIZE</div>
    <ul class="price-table">
      <li class="price-row"><span class="product">Card Keeper 1</span><span class="spec">3 5/16"x4 7/16" - Semi Rigid</span></li>
      <li class="price-row"><span class="product">Card Keeper 2</span><span class="spec">3"x4 1/2" - Semi Rigid</span></li>
      <li class="price-row"><span class="product">Card Keeper 3</span><span class="spec">3 1/3"x5 7/8" - Tall</span></li>
      <li class="price-row"><span class="product">Card Keeper 4</span><span class="spec">4 1/2"x 7 1/2" - Large</span></li>
      <li class="price-row"><span class="product">Card Keeper 5</span><span class="spec">3 1/2"x7 3/4" - Long</span></li>
      <li class="price-row"><span class="product">Top-Load 3x4 Clear (Standard Size)</span><span class="spec">3"x4" - 12 Pt.</span></li>
      <li class="price-row"><span class="product">Top-Load 3x4 “Rookie” Gold</span><span class="spec">3"x4" - 12 Pt.</span></li>
      <li class="price-row"><span class="product">Top-Load 3x4 Black Border</span><span class="spec">3"x4" - 12 Pt.</span></li>
      <li class="price-row"><span class="product">Top-Load 3x4 Blue Border</span><span class="spec">3"x4" - 12 Pt.</span></li>
      <li class="price-row"><span class="product">Top-Load 3x4 Red Border</span><span class="spec">3"x4" - 12 Pt.</span></li>
      <li class="price-row"><span class="product">Top-Load 3x4 White Border</span><span class="spec">3"x4" - 12 Pt.</span></li>
      <li class="price-row"><span class="product">Top-Load 3x4 1.5mm – 60 Pt.</span><span class="spec">3"x4" - 1.5mm</span></li>
      <li class="price-row"><span class="product">Top-Load 3x4 2.5mm – 100 Pt.</span><span class="spec">3"x4" - 2.5mm</span></li>
      <li class="price-row"><span class="product">Top-Load 3x4 3.5mm – 140 Pt.</span><span class="spec">3"x4" - 3.5mm</span></li>
      <li class="price-row"><span class="product">Top-Load 3x4 5mm – 190 Pt.</span><span class="spec">3"x4" - 5mm</span></li>
      <li class="price-row"><span class="product">Top-Load 3x4 7mm – 240 Pt.</span><span class="spec">3"x4" - 7mm</span></li>
      <li class="price-row"><span class="product">Top-Load 4x6 Photo</span><span class="spec">4"x6" - 15 Pt.</span></li>
      <li class="price-row"><span class="product">Top-Load 6x4 Side Load Photo</span><span class="spec">6"x4" - 15 Pt.</span></li>
    </ul>
  </div>
</body>
</html>
```